Bref créative
Velt Heating Ltd
business card & stationary package
Modern
Dorin Maleck, Owner
Government Certified Technician
(no address please)
Would also like a card made for:
Luc Brantley
info@veltheat.ca
www.veltheat.ca
Serving the North Shore of Vancouver since 1994
Air Conditioners
BBQs
Boilers
Firepits
Fireplaces
Furnaces
Gas Outlet Boxes
Patio Heaters
Pool Heaters
Heat Pumps
HRV Units
There is a spelling error under Dorin Maleck, Owner... there should be an 'n' in government.

```html
<!DOCTYPE html>
<html lang="en">
<head>
<meta charset="utf-8">
<title>Velt Heating Ltd – Stationery Package</title>
<link href="https://fonts.googleapis.com/css2?family=Open+Sans:wght@400;700&display=swap" rel="stylesheet">
<style>
:root{
  --stage-dark:#2f3133;
  --stage-light:#6e7173;
  --brand-blue:#1c8ad3;
  --brand-blue-deep:#0f5fa6;
  --brand-orange:#f28a1b;
  --paper:#ffffff;
  --ink:#3d3d3d;
  --ink-soft:#8a8a8a;
}
*{margin:0;padding:0;box-sizing:border-box}
html,body{width:1200px;height:209px;overflow:hidden}
body{
  font-family:"Open Sans",Arial,sans-serif;
  background:radial-gradient(ellipse at 50% 45%,var(--stage-light),var(--stage-dark) 75%);
  position:relative;
}
.piece{position:absolute;background:var(--paper);overflow:hidden;box-shadow:0 2px 5px rgba(0,0,0,.45)}
.wave{position:absolute;inset:0;width:100%;height:100%}
.brand{display:flex;align-items:center;gap:2px;color:var(--brand-blue);font-weight:700;white-space:nowrap;position:absolute}
.brand .dot{border-radius:50%;background:var(--brand-orange);flex:none}

/* business cards */
.card{width:50px;height:29px}
.card .brand{left:4px;top:4px;font-size:4px}
.card .brand .dot{width:4px;height:4px}
.card .who{position:absolute;left:4px;bottom:4px;font-size:2.4px;color:var(--ink);line-height:1.3}
.card-back .brand{left:50%;top:50%;transform:translate(-50%,-50%);font-size:5px;color:var(--paper)}
.card-back .brand .dot{width:5px;height:5px;background:var(--paper)}

/* letterheads */
.letterhead{width:118px;height:152px;top:33px}
.letterhead .brand{left:8px;top:9px;font-size:5px}
.letterhead .brand .dot{width:5px;height:5px}
.letterhead .body{position:absolute;left:8px;top:30px;width:86px;font-size:2.6px;color:var(--ink);line-height:1.6}
.letterhead .body p{margin-bottom:3px}
.letterhead .footer{position:absolute;left:8px;bottom:6px;font-size:2.4px;color:var(--ink-soft)}

/* envelopes */
.envelope{width:64px;height:30px}
.envelope .brand{left:4px;top:4px;font-size:3.8px}
.envelope .brand .dot{width:4px;height:4px}
.envelope-open{width:96px;height:58px;left:792px;top:58px;background:var(--brand-blue)}
.envelope-open .flap{position:absolute;left:0;top:0;width:100%;height:16px;background:var(--brand-orange)}
.envelope-open .brand{left:50%;top:28px;transform:translateX(-50%);font-size:5px;color:var(--paper)}
.envelope-open .brand .dot{width:5px;height:5px;background:var(--paper)}

/* folder */
.folder{left:905px;top:30px;width:130px;height:165px;background:var(--brand-blue)}
.folder .panel{position:absolute;right:8px;bottom:12px;width:64px;height:26px;background:var(--paper);border-radius:3px}
.folder .brand{right:14px;bottom:21px;font-size:7px}
.folder .brand .dot{width:6px;height:6px}
.folder-inner{left:1040px;top:40px;width:120px;height:150px;background:var(--brand-blue-deep)}
.folder-inner .pocket{position:absolute;left:0;bottom:0;width:100%;height:56px;background:var(--brand-blue)}
</style>
</head>
<body>

<!-- business cards -->
<div class="piece card" style="left:84px;top:40px">
  <svg class="wave" viewBox="0 0 50 29" preserveAspectRatio="none"><path d="M38 0 Q30 14 50 29 V0 Z" fill="var(--brand-blue)"/><path d="M42 0 Q36 10 50 22 V0 Z" fill="var(--brand-orange)"/></svg>
  <div class="brand"><span class="dot"></span>Velt Heating Ltd</div>
  <div class="who">Dorin Maleck, Owner<br>Government Certified Technician<br>info@veltheat.ca</div>
</div>
<div class="piece card" style="left:84px;top:76px">
  <svg class="wave" viewBox="0 0 50 29" preserveAspectRatio="none"><path d="M38 0 Q30 14 50 29 V0 Z" fill="var(--brand-blue)"/></svg>
  <div class="brand"><span class="dot"></span>Velt Heating Ltd</div>
  <div class="who">Luc Brantley<br>www.veltheat.ca<br>info@veltheat.ca</div>
</div>
<div class="piece card card-back" style="left:84px;top:112px;background:var(--brand-blue)">
  <div class="brand"><span class="dot"></span>Velt Heating Ltd</div>
</div>

<!-- letterheads -->
<div class="piece letterhead" style="left:146px">
  <svg class="wave" viewBox="0 0 118 152" preserveAspectRatio="none"><path d="M104 0 Q96 80 118 152 V0 Z" fill="var(--brand-blue)"/><path d="M0 146 Q60 138 118 150 V152 H0 Z" fill="var(--brand-orange)"/></svg>
  <div class="brand"><span class="dot"></span>Velt Heating Ltd</div>
  <div class="body"><p>Dear Client,</p><p>Thank you for choosing our team for your home heating and cooling service.</p><p>We look forward to working with you.</p><p>Sincerely,<br>Dorin Maleck</p></div>
  <div class="footer">info@veltheat.ca | www.veltheat.ca</div>
</div>
<div class="piece letterhead" style="left:274px">
  <svg class="wave" viewBox="0 0 118 152" preserveAspectRatio="none"><path d="M104 0 Q96 80 118 152 V0 Z" fill="var(--brand-blue)"/><path d="M0 146 Q60 138 118 150 V152 H0 Z" fill="var(--brand-orange)"/></svg>
  <div class="brand"><span class="dot"></span>Velt Heating Ltd</div>
  <div class="body"><p>Dear Client,</p><p>Thank you for choosing our team for your home heating and cooling service.</p><p>We look forward to working with you.</p><p>Sincerely,<br>Dorin Maleck</p></div>
  <div class="footer">info@veltheat.ca | www.veltheat.ca</div>
</div>
<div class="piece letterhead" style="left:402px">
  <svg class="wave" viewBox="0 0 118 152" preserveAspectRatio="none"><path d="M104 0 Q96 80 118 152 V0 Z" fill="var(--brand-blue)"/><path d="M0 146 Q60 138 118 150 V152 H0 Z" fill="var(--brand-orange)"/></svg>
  <div class="brand"><span class="dot"></span>Velt Heating Ltd</div>
  <div class="body"><p>Dear Client,</p><p>Thank you for choosing our team for your home heating and cooling service.</p><p>We look forward to working with you.</p><p>Sincerely,<br>Dorin Maleck</p></div>
  <div class="footer">info@veltheat.ca | www.veltheat.ca</div>
</div>
<div class="piece letterhead" style="left:530px">
  <svg class="wave" viewBox="0 0 118 152" preserveAspectRatio="none"><path d="M104 0 Q96 80 118 152 V0 Z" fill="var(--brand-blue)"/><path d="M0 146 Q60 138 118 150 V152 H0 Z" fill="var(--brand-orange)"/></svg>
  <div class="brand"><span class="dot"></span>Velt Heating Ltd</div>
  <div class="body"><p>Dear Client,</p><p>Thank you for choosing our team for your home heating and cooling service.</p><p>We look forward to working with you.</p><p>Sincerely,<br>Luc Brantley</p></div>
  <div class="footer">info@veltheat.ca | www.veltheat.ca</div>
</div>

<!-- envelopes -->
<div class="piece envelope" style="left:666px;top:44px">
  <svg class="wave" viewBox="0 0 64 30" preserveAspectRatio="none"><path d="M52 0 Q44 15 64 30 V0 Z" fill="var(--brand-blue)"/></svg>
  <div class="brand"><span class="dot"></span>Velt Heating Ltd</div>
</div>
<div class="piece envelope" style="left:666px;top:82px">
  <svg class="wave" viewBox="0 0 64 30" preserveAspectRatio="none"><path d="M52 0 Q44 15 64 30 V0 Z" fill="var(--brand-blue)"/></svg>
  <div class="brand"><span class="dot"></span>Velt Heating Ltd</div>
</div>
<div class="piece envelope" style="left:666px;top:120px">
  <svg class="wave" viewBox="0 0 64 30" preserveAspectRatio="none"><path d="M52 0 Q44 15 64 30 V0 Z" fill="var(--brand-blue)"/></svg>
  <div class="brand"><span class="dot"></span>Velt Heating Ltd</div>
</div>
<div class="piece envelope-open">
  <div class="flap"></div>
  <div class="brand"><span class="dot"></span>Velt Heating Ltd</div>
</div>
<div class="piece envelope" style="left:800px;top:128px;width:80px;height:34px">
  <div class="brand"><span class="dot"></span>Velt Heating Ltd</div>
</div>

<!-- presentation folder -->
<div class="piece folder-inner"><div class="pocket"></div></div>
<div class="piece folder">
  <svg class="wave" viewBox="0 0 130 165" preserveAspectRatio="none"><path d="M0 0 Q70 60 130 40 V0 Z" fill="var(--brand-blue-deep)" opacity=".5"/></svg>
  <div class="panel"></div>
  <div class="brand"><span class="dot"></span>Velt Heating Ltd</div>
</div>

</body>
</html>
```